Lantern Grove Films, wedding videographer

I'm looking to get a business card made inline with my current logo attached.<br/>I am looking for a business card that differs from the rest and is not plain and simple like most. <br/>I have seen some designs in B&W or designs were the letters are in Gold which I would like to see.<br/><br/>On the card I would like it to display the following details:<br/><br/>www.lanterngrovefilms.com<br/>"Instagram icon"@lanterngrovefilms<br/>"Facebook Icon" @lanterngrovefilms<br/>lanterngrovefilms@mailpost.example <br/>Ph: +353-87-612-0574<br/><br/>

Target Market(s)

Engaged Couples

Contact Information for Business Card

Name: Marta Wilkoren
Company: LanternGrove Films
PH: +353-87-612-0574
Instagram, Facebook @lanterngrovefilms

Font styles to use
Decorative
Script

Colors

Designer to choose colors to be used in the design.

Requirements
Should not have
• Plane design

```html
<!DOCTYPE html>
<html lang="en">
<head>
<meta charset="utf-8">
<title>Lantern Grove Films – Business Card</title>
<link rel="stylesheet" href="https://fonts.googleapis.com/css2?family=Roboto:wght@400;500;700&display=swap">
<style>
  :root {
    --backdrop: #1c1c1e;
    --card-black: #141516;
    --card-grey: #6f7072;
    --silver: #c9cacc;
    --silver-light: #f2f2f2;
    --white: #ffffff;
  }
  * { margin: 0; padding: 0; box-sizing: border-box; }
  html, body {
    width: 1200px; height: 874px; overflow: hidden;
    background: var(--backdrop);
    font-family: "Roboto", Arial, sans-serif;
  }
  .canvas {
    position: relative; width: 1200px; height: 874px;
  }
  .card {
    position: absolute; left: 290px;
    width: 620px; height: 354px;
    background: var(--card-black);
    overflow: hidden;
    box-shadow: 0 14px 30px rgba(0,0,0,0.55);
  }
  .card--front { top: 52px; }
  .card--back { top: 440px; }

  .brand-name {
    position: absolute;
    font-weight: 500;
    color: var(--silver);
    letter-spacing: 0.04em;
    white-space: nowrap;
  }
  .card--front .brand-name {
    left: 0; right: 0; top: 155px;
    text-align: center; font-size: 40px;
  }
  .card--back .brand-name {
    left: 40px; top: 92px; font-size: 30px;
  }

  .card-wave { position: absolute; inset: 0; }

  .contact {
    position: absolute; right: 36px; top: 222px;
    text-align: right; color: var(--white);
  }
  .contact__name {
    font-weight: 700; font-size: 21px; letter-spacing: 0.02em;
    margin-bottom: 14px; margin-right: 24px;
  }
  .contact__line {
    display: flex; justify-content: flex-end; align-items: center;
    gap: 10px; font-size: 15px; line-height: 21px;
  }
  .contact__icon { width: 13px; height: 13px; flex: none; }
</style>
</head>
<body>
<div class="canvas">

  <section class="card card--front">
    <div class="brand-name">Lantern Grove Films</div>
  </section>

  <section class="card card--back">
    <svg class="card-wave" viewBox="0 0 620 354" width="620" height="354" aria-hidden="true">
      <defs>
        <linearGradient id="swoosh" x1="0" y1="0" x2="1" y2="0">
          <stop offset="0" stop-color="#8d8e90"/>
          <stop offset="0.35" stop-color="#ffffff"/>
          <stop offset="0.7" stop-color="#d6d6d8"/>
          <stop offset="1" stop-color="#9a9b9d"/>
        </linearGradient>
      </defs>
      <path d="M0,212 C50,300 190,305 320,240 S520,148 620,145 L620,354 L0,354 Z" fill="var(--card-grey)"/>
      <path d="M0,212 C50,300 190,305 320,240 S520,148 620,145" fill="none" stroke="url(#swoosh)" stroke-width="6"/>
      <path d="M8,228 C70,305 200,305 320,252" fill="none" stroke="#3a3b3d" stroke-width="2"/>
    </svg>

    <div class="brand-name">Lantern Grove Films</div>

    <div class="contact">
      <div class="contact__name">MARTA WILKOREN</div>
      <div class="contact__line">
        <span>+353-87-612-0574</span>
        <svg class="contact__icon" viewBox="0 0 24 24" aria-hidden="true"><path fill="#fff" d="M6.6 10.8c1.4 2.8 3.8 5.1 6.6 6.6l2.2-2.2c.3-.3.7-.4 1-.2 1.1.4 2.3.6 3.6.6.6 0 1 .4 1 1V20c0 .6-.4 1-1 1C10.6 21 3 13.4 3 4c0-.6.4-1 1-1h3.5c.6 0 1 .4 1 1 0 1.3.2 2.5.6 3.6.1.3 0 .7-.2 1z"/></svg>
      </div>
      <div class="contact__line">
        <span>@lanterngrovefilms</span>
        <svg class="contact__icon" viewBox="0 0 24 24" aria-hidden="true"><circle cx="12" cy="12" r="11" fill="#fff"/></svg>
      </div>
      <div class="contact__line">
        <span>@lanterngrovefilms</span>
        <svg class="contact__icon" viewBox="0 0 24 24" aria-hidden="true"><circle cx="12" cy="12" r="10" fill="none" stroke="#fff" stroke-width="2.5"/></svg>
      </div>
    </div>
  </section>

</div>
</body>
</html>
```